The label Velombri Dijon Mustard

Hello everybody,
What we need : a design for a label of Dijon Mustard it's a new project and. What we're looking for : a european style with a warm vibe. The product's target : the North American.

The design must be elegant, modern and up market.don't hesitate to think outside the box.
we attached a file contain our logo. the logo for this product will be the main logo the third one.
and we attached a sizes and the inspiration design LUVETTE and CORBIN

Target Market(s)

North America

Logo Text

Velombri

Logo styles of interest
Wordmark Logo
Font styles to use
Serif
Script

Colors

Designer to choose colors to be used in the design.

Requirements
Must have
• -The brand ''Velombri'' and the logo is (the Main logo The Third one) attached file.
• - the name of the product, ''Dijon Mustard /Moutarde de Dijon/ ديجون الخردل'', in English, French and Arabic
• -The Lid will be red or black depend of your design.
• - the nutrition fact. Make a place and it will be changed by us.
• -Ingrediants:
• fr: eau, graines de MOUTARDE, vinaigre d'alcool, sel, acidifiant : acide citrique, conservateur : E224 (SULFITES).
• En: water, MUSTARD seeds, alcohol vinegar, salt, acidifier: citric acid, preservative: E224 (SULFITES).
• Ar: ماء ، بذور الخردل ، خل الكحول ، الملح ، محمض: حمض الستريك ، مواد حافظة: E224
• - the weight of 295g/ 250ml
• - conditioned by Sarl Velombri/conditionné par Sarl Velombri.
• -Slogan In French''Apportez le vrai goût à votre maison''
• -design must be elegant, modern and up market.
Nice to have
• -A minimalist design style
• -Design color: red or black.

```html
<!DOCTYPE html>
<html lang="en">
<head>
<meta charset="utf-8">
<title>Velombri Dijon Mustard – Red and Black options</title>
<link rel="stylesheet" href="https://fonts.googleapis.com/css2?family=Montserrat:wght@700&family=Cinzel:wght@400;700&family=Crimson+Text:wght@400;600&family=Amiri&display=swap">
<style>
  :root {
    --ink-black: #231f20;
    --mustard-red: #d52a26;
    --cream: #f7eea3;
    --white: #ffffff;
    --caption-grey: #7d7d7d;
    --page: #ffffff;
  }
  html, body {
    margin: 0;
    padding: 0;
    width: 1062px;
    height: 1200px;
    overflow: hidden;
    background: var(--page);
  }
  .sheet { display: block; width: 1062px; height: 1200px; }
  .caption {
    font-family: "Montserrat", Arial, sans-serif;
    font-weight: 700;
    fill: var(--caption-grey);
    text-anchor: middle;
  }
  .caption--title { font-size: 22px; }
  .caption--section { font-size: 21px; }
  .label--black .label-body { fill: var(--ink-black); }
  .label--red .label-body { fill: var(--mustard-red); }
  .brand-name {
    font-family: "Cinzel", Georgia, serif;
    font-weight: 700;
    font-size: 46px;
    fill: var(--cream);
    text-anchor: middle;
    letter-spacing: 1px;
  }
  .product-fr {
    font-family: "Cinzel", Georgia, serif;
    font-size: 17px;
    fill: var(--white);
    text-anchor: middle;
  }
  .product-en {
    font-family: "Cinzel", Georgia, serif;
    font-size: 29px;
    fill: var(--cream);
    text-anchor: middle;
  }
  .product-ar {
    font-family: "Amiri", "Times New Roman", serif;
    font-size: 21px;
    fill: var(--white);
    text-anchor: middle;
  }
  .net-weight {
    font-family: "Crimson Text", Georgia, serif;
    font-size: 15px;
    fill: var(--cream);
    text-anchor: middle;
  }
  .conditioned {
    font-family: "Crimson Text", Georgia, serif;
    font-size: 9.5px;
    fill: var(--white);
  }
  .slogan {
    font-family: "Cinzel", Georgia, serif;
    font-size: 11.5px;
    fill: var(--cream);
  }
  .back-heading {
    font-family: "Cinzel", Georgia, serif;
    font-size: 11px;
    fill: var(--white);
    text-anchor: middle;
  }
  .ingredients {
    font-family: "Crimson Text", Georgia, serif;
    font-size: 6.6px;
    fill: var(--white);
    text-anchor: middle;
  }
  .ingredients--ar { font-family: "Amiri", serif; font-size: 6.6px; }
  .nutrition-table { fill: none; stroke: var(--white); stroke-width: 0.8; }
  .lid-conditioned {
    font-family: "Crimson Text", Georgia, serif;
    font-size: 12px;
    fill: var(--cream);
  }
  .lid-slogan {
    font-family: "Cinzel", Georgia, serif;
    font-size: 12.5px;
    fill: var(--cream);
  }
</style>
</head>
<body>
<svg class="sheet" viewBox="0 0 1062 1200" xmlns="http://www.w3.org/2000/svg" xmlns:xlink="http://www.w3.org/1999/xlink">
  <defs>
    <path id="arc-conditioned" d="M -128 44 Q 0 109 120 50"/>
    <path id="arc-slogan" d="M -136 56 Q 0 122 120 66"/>
    <path id="arc-lid-top" d="M -128 18 A 129 129 0 1 1 128 18"/>
    <path id="arc-lid-bottom" d="M -112 64 A 129 129 0 0 0 112 64"/>
  </defs>

  <text class="caption caption--title" x="531" y="34">VELOMBRI® : Red and Black options</text>
  <text class="caption caption--section" x="310" y="187">FRONT LABEL</text>
  <text class="caption caption--section" x="734" y="187">BACK LABEL</text>

  <!-- Front label, black -->
  <g class="label label--black" transform="translate(318 342)">
    <ellipse class="label-body" cx="0" cy="0" rx="182" ry="104"/>
    <rect class="label-body" x="-132" y="-114" width="278" height="76" rx="34"/>
    <text class="brand-name" x="6" y="-62">Velombri</text>
    <text class="product-fr" x="0" y="-22">Moutarde de Dijon</text>
    <text class="product-en" x="0" y="8">Dijon Mustard</text>
    <text class="product-ar" x="0" y="30" direction="rtl">ديجون الخردل</text>
    <text class="net-weight" x="0" y="58">295g/ 250ml</text>
    <text class="conditioned"><textPath href="#arc-conditioned" startOffset="50%" text-anchor="middle">Conditioned by Sarl Velombri/Conditionné par Sarl Velombri</textPath></text>
    <text class="slogan"><textPath href="#arc-slogan" startOffset="50%" text-anchor="middle">APPORTEZ LE VRAI GOÛT À VOTRE MAISON</textPath></text>
  </g>

  <!-- Back label, black -->
  <g class="label label--black" transform="translate(735 342)">
    <ellipse class="label-body" cx="0" cy="0" rx="182" ry="104"/>
    <rect class="label-body" x="-132" y="-114" width="278" height="76" rx="34"/>
    <text class="brand-name" x="6" y="-62">Velombri</text>
    <text class="back-heading" x="0" y="-30">Ingredients:</text>
    <text class="ingredients" x="0" y="-18">Water, MUSTARD seeds, alcohol vinegar, salt, acidifier: citric acid, preservative: E224 (SULFITES).</text>
    <text class="ingredients" x="0" y="-6">Eau, graines de MOUTARDE, vinaigre d'alcool, sel, acidifiant : acide citrique, conservateur : E224 (SULFITES)</text>
    <text class="ingredients ingredients--ar" x="0" y="8" direction="rtl">ماء ، بذور الخردل ، خل الكحول ، الملح ، محمض: حمض الستريك ، مواد حافظة: E224</text>
    <text class="back-heading" x="0" y="28">Nutrition:</text>
    <g class="nutrition-table">
      <rect x="-108" y="33" width="216" height="44"/>
      <line x1="-108" y1="44" x2="108" y2="44"/>
      <line x1="-108" y1="55" x2="108" y2="55"/>
      <line x1="-108" y1="66" x2="108" y2="66"/>
      <line x1="0" y1="33" x2="0" y2="77"/>
    </g>
  </g>

  <!-- Front label, red -->
  <g class="label label--red" transform="translate(318 640)">
    <ellipse class="label-body" cx="0" cy="0" rx="182" ry="104"/>
    <rect class="label-body" x="-132" y="-114" width="278" height="76" rx="34"/>
    <text class="brand-name" x="6" y="-62">Velombri</text>
    <text class="product-fr" x="0" y="-22">Moutarde de Dijon</text>
    <text class="product-en" x="0" y="8">Dijon Mustard</text>
    <text class="product-ar" x="0" y="30" direction="rtl">ديجون الخردل</text>
    <text class="net-weight" x="0" y="58">295g/ 250ml</text>
    <text class="conditioned"><textPath href="#arc-conditioned" startOffset="50%" text-anchor="middle">Conditioned by Sarl Velombri/Conditionné par Sarl Velombri</textPath></text>
    <text class="slogan"><textPath href="#arc-slogan" startOffset="50%" text-anchor="middle">APPORTEZ LE VRAI GOÛT À VOTRE MAISON</textPath></text>
  </g>

  <!-- Back label, red -->
  <g class="label label--red" transform="translate(735 640)">
    <ellipse class="label-body" cx="0" cy="0" rx="182" ry="104"/>
    <rect class="label-body" x="-132" y="-114" width="278" height="76" rx="34"/>
    <text class="brand-name" x="6" y="-62">Velombri</text>
    <text class="back-heading" x="0" y="-30">Ingredients:</text>
    <text class="ingredients" x="0" y="-18">Water, MUSTARD seeds, alcohol vinegar, salt, acidifier: citric acid, preservative: E224 (SULFITES).</text>
    <text class="ingredients" x="0" y="-6">Eau, graines de MOUTARDE, vinaigre d'alcool, sel, acidifiant : acide citrique, conservateur : E224 (SULFITES)</text>
    <text class="ingredients ingredients--ar" x="0" y="8" direction="rtl">ماء ، بذور الخردل ، خل الكحول ، الملح ، محمض: حمض الستريك ، مواد حافظة: E224</text>
    <text class="back-heading" x="0" y="28">Nutrition:</text>
    <g class="nutrition-table">
      <rect x="-108" y="33" width="216" height="44"/>
      <line x1="-108" y1="44" x2="108" y2="44"/>
      <line x1="-108" y1="55" x2="108" y2="55"/>
      <line x1="-108" y1="66" x2="108" y2="66"/>
      <line x1="0" y1="33" x2="0" y2="77"/>
    </g>
  </g>

  <text class="caption caption--section" x="323" y="850">LID GRAPHIC</text>
  <text class="caption caption--section" x="733" y="850">LID GRAPHIC</text>

  <!-- Lid, black -->
  <g class="lid label--black" transform="translate(332 1034)">
    <circle class="label-body" cx="0" cy="0" r="146"/>
    <text class="lid-conditioned"><textPath href="#arc-lid-top" startOffset="50%" text-anchor="middle">Conditioned by Sarl Velombri/Conditionné par Sarl Velombri</textPath></text>
    <text class="brand-name" x="0" y="14">Velombri</text>
    <text class="lid-slogan"><textPath href="#arc-lid-bottom" startOffset="50%" text-anchor="middle">APPORTEZ LE VRAI GOÛT À VOTRE MAISON</textPath></text>
  </g>

  <!-- Lid, red -->
  <g class="lid label--red" transform="translate(738 1034)">
    <circle class="label-body" cx="0" cy="0" r="146"/>
    <text class="lid-conditioned"><textPath href="#arc-lid-top" startOffset="50%" text-anchor="middle">Conditioned by Sarl Velombri/Conditionné par Sarl Velombri</textPath></text>
    <text class="brand-name" x="0" y="14">Velombri</text>
    <text class="lid-slogan"><textPath href="#arc-lid-bottom" startOffset="50%" text-anchor="middle">APPORTEZ LE VRAI GOÛT À VOTRE MAISON</textPath></text>
  </g>
</svg>
</body>
</html>
```